Redesign of a facility management homepage

We need a redesign/an improved design of the facility management homepage (http://www.kolvenhaus-drefling.de/).
This websites offers detailed information on the "About us" as company, the "Services" provided and special information on facility and strata management. We would like to keep the structure of the website.
We need ideas/designs how this website could look more modern and confidential and appealing/pleasant for visitors at the same time and not losing the main purpose of information distribution.
The green color must be used since this is the basic color from our logo.
The blue in the background of the logo ist optional. So feel to use it or not.
We need no coding only design (.psd or as .ai)
Industry/Entity Type
It Company
Look and feel
Each slider illustrates characteristics of the customer's brand and the style your logo design should communicate.

```html
<!DOCTYPE html>
<html lang="de">
<head>
<meta charset="utf-8">
<title>Kolvenhaus Gebäudeservice GmbH Drefling</title>
<link href="https://fonts.googleapis.com/css2?family=Lato:wght@300;400;700&family=Bebas+Neue&family=Noto+Serif:ital@1&display=swap" rel="stylesheet">
<style>
:root{
  --green:#7ad100;
  --green-dark:#3f9a1a;
  --green-text:#4a9a1f;
  --navy:#2b4565;
  --ink:#111;
  --grey-light:#ebebeb;
  --tile-frame:#e6e6e6;
  --white:#fff;
}
*{margin:0;padding:0;box-sizing:border-box}
html,body{width:1200px;height:1000px;overflow:hidden;background:var(--white);font-family:"Lato",sans-serif;color:var(--ink)}
.page{position:relative;width:1200px;height:1000px}
.brand{position:absolute;left:124px;top:44px;display:flex;align-items:center;gap:10px}
.brand-mark{width:22px;height:22px;background:var(--green-dark)}
.brand-name{font-size:26px;font-weight:700;color:var(--green-dark)}
.tagline{position:absolute;left:312px;top:36px;font-size:20px;font-weight:700;line-height:26px;color:var(--ink)}
.contact{position:absolute;left:928px;top:12px;font-size:13.5px;font-weight:700;line-height:17px}
.contact-title{display:flex;align-items:center;gap:8px;font-size:29px;color:var(--navy);margin-bottom:6px}
.contact-title svg{display:block}
.nav{position:absolute;left:0;top:118px;width:1200px;height:52px;background:linear-gradient(#fbfbfb,#e3e3e3);border:1px solid #d4d4d4}
.nav ul{list-style:none;display:flex;position:absolute;left:205px;top:0;height:51px}
.nav li{padding:0 16px 0 14px;font-size:22px;font-weight:700;color:var(--green-text);line-height:54px;border-right:1px solid #c8c8c8}
.nav li:last-child{border:none}
.nav li.active{background:linear-gradient(#84cf32,#5fae17);color:var(--white)}
.hero-band{position:absolute;left:0;top:185px;width:1200px;height:220px;background:var(--green)}
.slider{position:absolute;left:268px;top:196px;width:665px;height:290px;background:#f7f7f7;border:1px solid #ddd;box-shadow:0 10px 18px rgba(0,0,0,.2)}
.slide-photo{position:absolute;left:8px;top:8px;width:650px;height:274px;background:linear-gradient(#b9a58b 0%,#d9dbd8 40%,#9a958d 70%,#6d6660 100%)}
.arrow{position:absolute;top:136px;width:19px;height:22px;background:rgba(255,255,255,.85);display:flex;align-items:center;justify-content:center}
.arrow.prev{left:0}.arrow.next{right:0}
.caption{position:absolute;left:26px;top:173px;width:434px;height:73px;background:rgba(200,200,200,.82);border-radius:4px;padding:6px 12px}
.caption h2{font-size:16px;font-weight:700;color:#666}
.caption p{font-size:8.5px;line-height:10.5px;color:#444}
.dots{position:absolute;left:280px;top:253px;width:90px;height:21px;background:#ececec;border-radius:4px 4px 0 0;display:flex;gap:5px;justify-content:center;align-items:center}
.dots span{width:9px;height:9px;border-radius:50%;background:#aaa}
.dots span.on{background:var(--green-dark)}
.tile{position:absolute;top:519px;width:177px;height:158px;background:var(--tile-frame);border:1px solid #d6d6d6;box-shadow:0 2px 3px rgba(0,0,0,.3)}
.tile-photo{position:absolute;left:10px;top:7px;width:173px;height:141px}
.tile-label{position:absolute;left:10px;top:120px;width:173px;height:28px;background:rgba(255,255,255,.75);text-align:center;font-size:14.5px;line-height:28px;font-weight:400}
.quote{position:absolute;left:226px;top:713px;font-family:"Noto Serif",serif;font-style:italic;font-size:17px;line-height:22px;color:#222}
.quote-author{position:absolute;left:345px;top:786px;font-size:17px;font-weight:700}
.quote-author b{color:var(--green-dark)}
.imprint{position:absolute;left:640px;top:698px;font-size:15px;font-weight:300;line-height:19.5px}
.footer-line{position:absolute;left:0;top:859px;width:1200px;height:7px;border-top:3px solid #3ec27a;border-bottom:2px solid #3ec27a}
.footer{position:absolute;left:0;top:866px;width:1200px;height:134px;background:var(--grey-light)}
.copyright{position:absolute;left:132px;top:58px;font-family:"Bebas Neue",sans-serif;font-size:22px;letter-spacing:.5px}
.social{position:absolute;left:860px;top:53px;display:flex;gap:14px}
.social span{width:32px;height:32px;border-radius:3px;background:var(--green-dark);box-shadow:0 1px 2px rgba(0,0,0,.3)}
</style>
</head>
<body>
<div class="page">
  <header>
    <div class="brand"><span class="brand-mark"></span><span class="brand-name">Kolvenhaus</span></div>
    <p class="tagline">Kolvenhaus Gebäudeservice GmbH Drefling<br>Ihr Partner vor Ort.</p>
    <div class="contact">
      <div class="contact-title">Kontakt
        <svg width="28" height="28" viewBox="0 0 28 28"><rect width="28" height="28" rx="4" fill="#7ad100"/><path d="M10 6c-2 1-3 3-2 6 1 4 5 9 9 10 2 1 4 0 5-2l-3-3-2 1c-2-1-4-4-5-6l1-2z" fill="#fff"/></svg>
      </div>
      Tel.: 0 41 52 / 38 70 12<br>Fax: 0 41 52 / 38 70 19<br>info@kolvenhaus-drefling.de
    </div>
  </header>

  <nav class="nav">
    <ul>
      <li class="active">Wir über uns</li>
      <li>Gebäudemanagement</li>
      <li>Gebäudeverwaltung</li>
      <li>Vermietung</li>
    </ul>
  </nav>

  <div class="hero-band"></div>
  <section class="slider">
    <div class="slide-photo" role="img" aria-label="Fuhrpark: weiße Servicefahrzeuge auf gepflastertem Hof">
      <div class="arrow prev"><svg width="8" height="10"><path d="M6 1 2 5l4 4" stroke="#555" stroke-width="2" fill="none"/></svg></div>
      <div class="arrow next"><svg width="8" height="10"><path d="M2 1l4 4-4 4" stroke="#555" stroke-width="2" fill="none"/></svg></div>
      <div class="caption">
        <h2>Unser Fuhrpark</h2>
        <p>Lorem ipsum dolor sit amet, consectetuer adipiscing elit, sed diam nonummy nibh euismod tincidunt ut laoreet dolore magna aliquam erat volutpat. Ut wisi enim ad minim veniam, quis nostrud exerci tation ullamcorper.</p>
      </div>
      <div class="dots"><span></span><span></span><span class="on"></span><span></span><span></span><span></span></div>
    </div>
  </section>

  <div class="tile" style="left:161px"><div class="tile-photo" role="img" aria-label="Mitarbeiterin im Kundenservice mit Headset" style="background:linear-gradient(90deg,#c9a48a,#e9d5c6 60%,#f2ece6)"></div><div class="tile-label">Störung online melden</div></div>
  <div class="tile" style="left:389px"><div class="tile-photo" role="img" aria-label="Tastatur mit grüner Kontakttaste" style="background:linear-gradient(135deg,#eee,#bdbdbd 45%,#2f9e3f 55%,#555)"></div><div class="tile-label">Kontakt</div></div>
  <div class="tile" style="left:617px"><div class="tile-photo" role="img" aria-label="Bauplan mit Taschenrechner" style="background:linear-gradient(135deg,#f3f3f3,#d2d4d4 60%,#9a9c9c)"></div><div class="tile-label">Links</div></div>
  <div class="tile" style="left:845px"><div class="tile-photo" role="img" aria-label="Hände schützen ein kleines Hausmodell" style="background:linear-gradient(90deg,#d9a083,#f0e6e0 40%,#d0503a 55%,#f0e6e0 65%,#d9a083)"></div><div class="tile-label">Impressum</div></div>

  <blockquote class="quote">“Lorem ipsum dolor sit amet,<br>consectetuer adipiscing elit, sed diam<br>nonummy nibh euismod tincidunt”</blockquote>
  <p class="quote-author"><b>Tom Barker,</b> USA</p>

  <address class="imprint" style="font-style:normal">
    Kolvenhaus Gebäudeservice GmbH<br><br>
    Lindenplatz 14 in 04712 Drefling<br>
    vertreten durch Frau Sabine Wernitz,<br>
    Geschäftsführerin<br><br>
    AG Drefling, HR.Nr.: HBR 40217
  </address>

  <div class="footer-line"></div>
  <footer class="footer">
    <p class="copyright">©2014. All rights reserved</p>
    <div class="social" aria-label="Soziale Netzwerke"><span></span><span></span><span></span><span></span><span></span></div>
  </footer>
</div>
</body>
</html>
```